Kelvane Plumbing Business cards

Company is Kelvane Plumbing.
name Dashel Morrowby, I am a plumber, drainer, gasfitter and roofer
Mobile: 0431 906 154
Email address: info@kelvaneplumbing.example (check out my website for some ideas)
Website: www.kelvaneplumbing.example
ABN: 82 916 203 471
LIC: 604517K

I am reliable all round plumber. I am a 24 hour emergency service. Kelvane Plumbing is a professional plumbing service in the Illawarra, South Coast, Southern Sydney and Southern Highland regions of NSW. We offer a 24 hour emergency service for piece of mind to our customers. Call us now to see how we can help you. Kelvane Plumbing approaches every job with attention to detail and excellent customer service. With our superior workmanship you can be confident that the job will be done right the first time around. You can rest assured with results that are guaranteed to last.

Target Market(s)

the general public

Contact Information for Business Card

look up website for some ideas something with similar colours to logo and new modern and to catch the eye.

Colors
fdfdfd
ffffff
000000
7f7f7f
aaaaaa
33a6d7
0492cd

Requirements
Must have
• all contact details
• company- Kelvane Plumbing
• name- Dashel Morrowby
• number mobile- 0431 906 154
• Email address- info@kelvaneplumbing.example
• Website- www.kelvaneplumbing.example
• ABN- 82 916 203 471
• LIC- 604517K

```html
<!DOCTYPE html>
<html lang="en">
<head>
<meta charset="utf-8">
<title>Kelvane Plumbing Business Cards</title>
<link href="https://fonts.googleapis.com/css2?family=Mulish:wght@400;600;800&display=swap" rel="stylesheet">
<style>
  :root {
    --bg: #d8d8d8;
    --card: #000000;
    --white: #ffffff;
    --grey: #7f7f7f;
    --grey-dark: #2b2b2b;
    --blue: #33a6d7;
    --blue-deep: #0492cd;
    --text-font: "Mulish", sans-serif;
  }
  * { margin: 0; padding: 0; box-sizing: border-box; }
  html, body {
    width: 1200px; height: 800px; overflow: hidden;
    background: var(--bg);
    font-family: var(--text-font);
  }
  .card {
    position: absolute; top: 250px;
    width: 540px; height: 300px;
    background: var(--card);
    overflow: hidden;
  }
  .card--contact { left: 40px; }
  .card--brand { left: 620px; }

  .tool-decor {
    position: absolute;
    background: var(--grey-dark);
  }
  .card--contact .tool-decor--top { left: 0; top: 0; width: 44px; height: 74px; clip-path: polygon(0 0,100% 0,100% 40%,60% 100%,0 100%); }
  .card--contact .tool-decor--bottom { right: 0; bottom: 0; width: 76px; height: 66px; clip-path: polygon(40% 0,100% 45%,100% 100%,0 100%,0 20%); }
  .card--brand .tool-decor--top { left: 0; top: 0; width: 114px; height: 90px; clip-path: polygon(0 0,100% 0,60% 100%,0 100%); }
  .card--brand .tool-decor--bottom { right: 0; bottom: 0; width: 112px; height: 84px; clip-path: polygon(35% 0,100% 30%,100% 100%,0 100%); }

  .brand-mark {
    position: absolute; left: 150px; top: 150px;
    transform: translate(-50%, -50%);
    text-align: center;
    color: var(--blue);
    font-weight: 800;
    letter-spacing: 0.06em;
    line-height: 1.15;
  }
  .brand-mark__dot {
    display: block; width: 14px; height: 14px; margin: 0 auto 10px;
    border-radius: 50%; background: var(--blue);
  }
  .brand-mark__name { font-size: 22px; }

  .divider {
    position: absolute; left: 272px; top: 52px;
    width: 1px; height: 196px; background: var(--blue-deep);
  }
  .contact {
    position: absolute; left: 316px; top: 56px;
    color: var(--white);
  }
  .contact__name {
    color: var(--blue); font-size: 19px; font-weight: 400;
    margin-bottom: 30px;
  }
  .contact__list { list-style: none; }
  .contact__item {
    display: flex; align-items: center; gap: 12px;
    font-size: 11px; height: 26px;
  }
  .contact__item svg { width: 12px; height: 12px; flex: none; }
  .contact__legal {
    margin-top: 22px; font-size: 11px; line-height: 18px;
  }

  .brand-title {
    position: absolute; left: 0; right: 0; top: 112px;
    text-align: center;
    color: var(--blue);
    font-weight: 800; font-size: 40px; letter-spacing: 0.04em;
  }
  .services {
    position: absolute; left: 0; right: 0; top: 212px;
    display: flex; justify-content: center; align-items: center;
    color: var(--white); font-size: 15px; font-weight: 600;
  }
  .services__sep {
    width: 2px; height: 20px; background: var(--white); margin: 0 8px;
  }
  .tagline {
    position: absolute; left: 0; right: 0; top: 244px;
    text-align: center; color: var(--blue); font-size: 17px;
  }
</style>
</head>
<body>

<section class="card card--contact">
  <div class="tool-decor tool-decor--top" role="img" aria-label="Faint pipe wrench decoration"></div>
  <div class="tool-decor tool-decor--bottom" role="img" aria-label="Faint pipe wrench decoration"></div>

  <div class="brand-mark">
    <span class="brand-mark__dot"></span>
    <div class="brand-mark__name">KELVANE<br>PLUMBING</div>
  </div>

  <div class="divider"></div>

  <div class="contact">
    <h1 class="contact__name">Dashel Morrowby</h1>
    <ul class="contact__list">
      <li class="contact__item">
        <svg viewBox="0 0 12 12"><rect x="3" y="0.5" width="6" height="11" rx="1" fill="none" stroke="#fff"/><line x1="5" y1="9.5" x2="7" y2="9.5" stroke="#fff"/></svg>
        0431 906 154
      </li>
      <li class="contact__item">
        <svg viewBox="0 0 12 12"><rect x="1" y="3" width="10" height="7" fill="#fff"/><path d="M1 3 L6 7 L11 3" fill="none" stroke="#000" stroke-width="1"/></svg>
        info@kelvaneplumbing.example
      </li>
      <li class="contact__item">
        <svg viewBox="0 0 12 12" fill="none" stroke="#fff" stroke-width="0.9"><circle cx="6" cy="6" r="5"/><ellipse cx="6" cy="6" rx="2.2" ry="5"/><line x1="1" y1="6" x2="11" y2="6"/></svg>
        www.kelvaneplumbing.example
      </li>
    </ul>
    <p class="contact__legal">Lic. 604517K<br>ABN: 82 916 203 471</p>
  </div>
</section>

<section class="card card--brand">
  <div class="tool-decor tool-decor--top" role="img" aria-label="Crossed pipe wrenches decoration"></div>
  <div class="tool-decor tool-decor--bottom" role="img" aria-label="Crossed pipe wrenches decoration"></div>

  <h2 class="brand-title">KELVANE PLUMBING</h2>

  <div class="services">
    <span>Plumbing</span><span class="services__sep"></span>
    <span>Drainage</span><span class="services__sep"></span>
    <span>Gas Fitting</span><span class="services__sep"></span>
    <span>Roofing</span>
  </div>
  <p class="tagline">24/7 Emergency Services</p>
</section>

</body>
</html>
```